Design business card for Bright Harbour Coaching!

I am a personal development coach (like a life coach) and corporate trainer and need a professionally designed double sided business card.

It needs to contain the business logo (I'm happy for the designer to choose the layout of the logo as I am still working out the best option myself) and the following information:

Tamsin Varga
Personal Development Coach and Trainer

+61 (0)452 819 407 (written that way)
tamsin@bright-harbour.com

www.bright-harbour.com

```html
<!DOCTYPE html>
<html lang="en">
<head>
<meta charset="utf-8">
<title>Bright Harbour Coaching – Business Card</title>
<link href="https://fonts.googleapis.com/css2?family=Cinzel:wght@400&family=PT+Serif:ital@0;1&display=swap" rel="stylesheet">
<style>
  :root {
    --backdrop: #b3b4b8;
    --card: #f8fafa;
    --ink: #5a5d62;
    --teal: #1f7a84;
    --teal-bright: #1596a2;
    --body: #4d5055;
  }
  html, body {
    margin: 0;
    width: 1194px;
    height: 1200px;
    overflow: hidden;
    background: var(--backdrop);
  }
  .canvas { position: relative; width: 1194px; height: 1200px; }
  .card {
    position: absolute;
    left: 204px;
    width: 786px;
    height: 474px;
    background: var(--card);
  }
  .card--front { top: 109px; }
  .card--back { top: 616px; }

  .brand-dot {
    position: absolute;
    border-radius: 50%;
    background: var(--teal-bright);
  }
  .brand-name {
    position: absolute;
    margin: 0;
    font-family: "Cinzel", serif;
    font-weight: 400;
    color: var(--ink);
    white-space: nowrap;
    letter-spacing: 1px;
  }
  .card--front .brand-dot { width: 70px; height: 70px; left: 358px; top: 160px; }
  .card--front .brand-name {
    left: 0; right: 0; top: 272px;
    text-align: center;
    font-size: 38px;
  }
  .card--back .brand-dot { width: 62px; height: 62px; left: 85px; top: 137px; }
  .card--back .divider {
    position: absolute;
    left: 181px; top: 99px;
    width: 1px; height: 126px;
    background: #9fc8cc;
  }
  .card--back .brand-name {
    left: 193px; top: 138px;
    font-size: 30px;
  }

  .holder { position: absolute; left: 55px; top: 294px; font-family: "PT Serif", serif; }
  .holder__name { margin: 0; font-size: 26px; color: var(--teal); font-weight: 400; }
  .holder__role { margin: 12px 0 0; font-size: 17px; line-height: 21px; font-style: italic; color: var(--body); }

  .contact {
    position: absolute; left: 370px; top: 292px;
    margin: 0; padding: 0; list-style: none;
    font-family: "PT Serif", serif; font-size: 20px; color: var(--body);
  }
  .contact li { display: flex; align-items: center; height: 31.5px; }
  .contact svg { width: 20px; height: 20px; margin-right: 20px; fill: var(--teal); flex: none; }
</style>
</head>
<body>
<div class="canvas">
  <section class="card card--front">
    <span class="brand-dot"></span>
    <h1 class="brand-name">BRIGHT HARBOUR COACHING</h1>
  </section>

  <section class="card card--back">
    <span class="brand-dot"></span>
    <span class="divider"></span>
    <h2 class="brand-name">BRIGHT HARBOUR COACHING</h2>

    <div class="holder">
      <h3 class="holder__name">Tamsin Varga</h3>
      <p class="holder__role">Personal Development Coach<br>and Trainer</p>
    </div>

    <ul class="contact">
      <li>
        <svg viewBox="0 0 20 20" aria-hidden="true"><path d="M2 6c0-2 3-3 8-3s8 1 8 3v2h-4V6.5c-1-.5-7-.5-8 0V8H2z"/><path d="M5 9h10l2 8H3z"/><circle cx="10" cy="13" r="2" fill="#f8fafa"/></svg>
        +61 (0)452 819 407
      </li>
      <li>
        <svg viewBox="0 0 20 20" aria-hidden="true"><path d="M1 4h18v12H1z"/><path d="M2 5l8 6 8-6M2 15l6-5M18 15l-6-5" stroke="#f8fafa" stroke-width="1.5" fill="none"/></svg>
        tamsin@bright-harbour.com
      </li>
      <li>
        <svg viewBox="0 0 20 20" aria-hidden="true"><circle cx="10" cy="10" r="8"/><path d="M2 10h16M10 2c-4 4-4 12 0 16M10 2c4 4 4 12 0 16M4 6h12M4 14h12" stroke="#f8fafa" stroke-width="1.1" fill="none"/></svg>
        www.bright-harbour.com
      </li>
    </ul>
  </section>
</div>
</body>
</html>
```